Property Management Company Business Cards

Need business cards for a property management company located in Michigan. We manage houses for clients all over the world. Young and modern company, looking for eye catching design. Please work with the attached logo.

Industry/Entity Type

Property Management

Requirements
Must have
• Need lines for address, telephone number, fax number, web site.

Also lines for name, and job title

```html
<!DOCTYPE html>
<html lang="en">
<head>
<meta charset="utf-8">
<title>Lakeshore Harbor Management – Business Cards</title>
<link rel="stylesheet" href="https://fonts.googleapis.com/css2?family=Lato:wght@400;700;900&display=swap">
<style>
  :root {
    --bg: #dfe5e8;
    --card: #ffffff;
    --ink: #3a3b3f;
    --ink-soft: #56575b;
    --accent: #1aa7ec;
    --shadow: rgba(30, 45, 55, 0.18);
  }
  * { margin: 0; padding: 0; box-sizing: border-box; }
  html, body {
    width: 1200px; height: 960px; overflow: hidden;
    background: var(--bg);
    font-family: "Lato", sans-serif;
    color: var(--ink);
  }
  .sheet {
    width: 1200px; height: 960px;
    display: flex; flex-direction: column; align-items: center; justify-content: center;
    gap: 70px;
  }
  .card {
    position: relative;
    width: 600px; height: 343px;
    background: var(--card);
    box-shadow: 0 10px 30px var(--shadow);
    overflow: hidden;
  }

  /* front */
  .brand-block {
    position: absolute; left: 48px; top: 70px; width: 200px;
    display: flex; flex-direction: column; align-items: center; gap: 18px;
  }
  .brand-dot { width: 110px; height: 110px; border-radius: 50%; background: var(--accent); }
  .brand-name {
    font-weight: 900; font-size: 22px; color: var(--ink);
    text-align: center; line-height: 1.15; text-transform: uppercase;
  }
  .contact {
    position: absolute; left: 300px; top: 46px;
  }
  .person-name { font-size: 25px; font-weight: 400; color: var(--ink-soft); letter-spacing: 0.3px; }
  .person-title { font-size: 15px; color: var(--ink-soft); margin-top: 4px; }
  .contact-lines { list-style: none; margin-top: 30px; }
  .contact-lines li {
    display: flex; align-items: center; gap: 10px;
    font-size: 15px; color: var(--ink-soft); line-height: 24px;
  }
  .contact-lines svg { width: 14px; height: 14px; flex: none; }
  .web { font-weight: 700; color: var(--ink); }
  .web .hl { color: var(--accent); }
  .address { margin-top: 26px; font-size: 15px; line-height: 22px; color: var(--ink-soft); }
  .front-stripe {
    position: absolute; left: 0; right: 0; bottom: 28px;
    height: 6px; background: var(--accent);
  }

  /* back */
  .back-brand {
    position: absolute; left: 0; right: 0; top: 120px;
    display: flex; align-items: center; justify-content: center; gap: 18px;
  }
  .back-dot { width: 58px; height: 58px; border-radius: 50%; background: var(--accent); flex: none; }
  .back-name {
    font-weight: 900; font-size: 30px; color: var(--ink);
    text-transform: uppercase; line-height: 1.1;
  }
  .back-footer {
    position: absolute; left: 0; right: 0; bottom: 34px;
    display: flex; align-items: center; justify-content: flex-end; gap: 10px;
  }
  .back-web {
    font-weight: 700; font-size: 14px; letter-spacing: 3.5px; color: var(--ink);
  }
  .back-web .hl { color: var(--accent); }
  .back-rule { width: 180px; height: 5px; background: var(--accent); }
</style>
</head>
<body>
<main class="sheet">

  <section class="card card-front" aria-label="Business card front">
    <div class="brand-block">
      <div class="brand-dot"></div>
      <div class="brand-name">Lakeshore<br>Harbor</div>
    </div>

    <div class="contact">
      <h1 class="person-name">DANA WHITFIELD</h1>
      <p class="person-title">Operation Manager</p>

      <ul class="contact-lines">
        <li>
          <svg viewBox="0 0 14 14" aria-label="Telephone"><rect x="2" y="1" width="10" height="12" rx="1.5" fill="none" stroke="var(--accent)" stroke-width="1.5"/><line x1="5" y1="4" x2="9" y2="4" stroke="var(--accent)" stroke-width="1.3"/><line x1="5" y1="7" x2="9" y2="7" stroke="var(--accent)" stroke-width="1.3"/><line x1="5" y1="10" x2="9" y2="10" stroke="var(--accent)" stroke-width="1.3"/></svg>
          (221) 30 412 58 16
        </li>
        <li>
          <svg viewBox="0 0 14 14" aria-label="Fax"><rect x="4" y="1" width="6" height="4" fill="none" stroke="var(--accent)" stroke-width="1.3"/><rect x="1" y="5" width="12" height="6" rx="1" fill="var(--accent)"/><rect x="4" y="9" width="6" height="4" fill="#fff" stroke="var(--accent)" stroke-width="1.3"/></svg>
          (221) 70 285 41 93
        </li>
        <li>
          <svg viewBox="0 0 14 14" aria-label="Website"><rect x="3.5" y="1" width="7" height="12" rx="3.5" fill="none" stroke="var(--accent)" stroke-width="1.4"/><line x1="7" y1="2.5" x2="7" y2="5.5" stroke="var(--accent)" stroke-width="1.4"/></svg>
          <span class="web">www.<span class="hl">lakeshore-harbor</span>.com</span>
        </li>
      </ul>

      <p class="address">Rue des Tilleuls - Parc Vert<br>BP 512 - City, Country</p>
    </div>

    <div class="front-stripe"></div>
  </section>

  <section class="card card-back" aria-label="Business card back">
    <div class="back-brand">
      <div class="back-dot"></div>
      <div class="back-name">Lakeshore Harbor<br>Management</div>
    </div>
    <div class="back-footer">
      <span class="back-web">www.<span class="hl">lakeshore-harbor</span>.com</span>
      <div class="back-rule"></div>
    </div>
  </section>

</main>
</body>
</html>
```